Inspirational Quote Poster for Employees

For this project, we need a simple yet high-impact poster template that will be customized for each of our employees with a personalized inspirational quote and color scheme. This template should allow us to quickly and easily customize the text and colors in the poster without a lot of effort.

The poster design should consist of:
- A stylized text area to contain the main text of the quote
- A separate text area to contain the source of quote
- A background that complements the color and style of the text

Text may use different typographic effects (such as color, stroke weight, italicization, font size changes, drop shadows) to draw attention to words in the quote; the source of the quote may be formatted the same as the main text of the quote, or may be formatted differently to distinguish it from the main quote.

The background may be simply a single color, subtle texture, gradients, halftone effects, or other color/texture effects may be used to complement the text.

Examples of the types of posters envisioned by this project:
- http://www.pinvelora.example/marcusdtelford/quillbase-job-1/

Sample quotes to use to build your poster - choose whichever one you want, but be certain that the poster design will handle both long and short quotes:
- "Happiness in intelligent people is the rarest thing I know" - Walden Prosket
- "Wanting to be someone else is a waste of the person you are." - Rolf Dintey
- "Experience is not what happens to you. It is what you do with what happens to you." - Ferris Mundell
- "Simplicity is the ultimate in sophistication." - Rinaldo de Pavesco
- "You will get all you want in life if you help enough other people get what they want." - Tad Pomfrey
- "Hell, there are no rules here — we're trying to accomplish something." - Gareth Vullane

Industry/Entity Type

Quote

Requirements
Must have
• Final deliverable must be:
• - Formatted for an 18” x 24” poster (in portrait orientation)
• - Delivered in Adobe InDesign, Adobe Illustrator, or Extended PostScript format
• - Use CMYK color mode
• - Be print-ready at 300dpi resolution
• - Include any fonts used in the template

```html
<!DOCTYPE html>
<html lang="en">
<head>
<meta charset="utf-8">
<title>Quote Poster – Simplicity</title>
<link rel="stylesheet" href="https://fonts.googleapis.com/css2?family=Anton&family=Open+Sans:wght@300&display=swap">
<style>
  :root {
    --page-bg: #ffffff;
    --poster-bg: #231f20;
    --ink: #ffffff;
  }
  html, body {
    margin: 0;
    padding: 0;
    width: 1200px;
    height: 1000px;
    overflow: hidden;
    background: var(--page-bg);
  }
  .canvas {
    position: relative;
    width: 1200px;
    height: 1000px;
  }
  .poster {
    position: absolute;
    left: 306px;
    top: 80px;
    width: 594px;
    height: 842px;
    background: var(--poster-bg);
    overflow: hidden;
  }
  .poster svg {
    display: block;
    width: 594px;
    height: 842px;
  }
  .quote-strong {
    font-family: "Anton", "Impact", sans-serif;
    fill: var(--ink);
  }
  .quote-light {
    font-family: "Open Sans", "Helvetica Neue", sans-serif;
    font-weight: 300;
    fill: var(--ink);
  }
  .quote-source {
    font-family: "Open Sans", "Helvetica Neue", sans-serif;
    font-weight: 300;
    fill: var(--ink);
  }
</style>
</head>
<body>
  <div class="canvas">
    <div class="poster">
      <svg viewBox="0 0 594 842" xmlns="http://www.w3.org/2000/svg" role="img" aria-label="Simplicity is the ultimate in sophistication. Rinaldo de Pavesco">
        <text class="quote-strong" transform="translate(-10 292) rotate(-11)"
              font-size="148" textLength="556" lengthAdjust="spacingAndGlyphs">SIMPLICITY</text>
        <text class="quote-light" transform="translate(14 380) rotate(-11)"
              font-size="78" textLength="572" lengthAdjust="spacingAndGlyphs">IS THE ULTIMATE IN</text>
        <text class="quote-strong" transform="translate(34 485) rotate(-11)"
              font-size="112" textLength="590" lengthAdjust="spacingAndGlyphs">SOPHISTICATION</text>
        <text class="quote-source" transform="translate(364 470) rotate(-11)"
              font-size="21">Rinaldo de Pavesco</text>
      </svg>
    </div>
  </div>
</body>
</html>
```